Personal Business Card

Looking for a clean and modern personal business card. Basically I need something catchy to give to potential clients and people I meet. I do a lot of freelancing (from DJ'ing to wedding videography, but its mostly on the event side of things) so it's more-so about selling myself rather than identifying with a company. I'm starting to meet more people that I want to work with after meeting them so I'm revamping my business cards.

I'm looking for a clean and modern design- I know that's really vague but I'm fine with anything ranging from a symbol to just a fancy version of my name.

Details I need on the front:
Gerald Minsky
gerald@geraldminsky-demo.com
(555) 902-4416

On the back I'd like to have something simple like "Nice to have met you today" or "Great meeting you".

UPDATE 9/27 Noon: My apologies for not putting it up before- I'm definitely looking for full color. Doesn't have to be a rainbow but I am looking for the least amount of blank white as possible.

UPDATE 10/1: Really impressed with what I've been getting so far and I'm working on giving everyone feedback- if your design is still up then you're still in the run. Looking for something more unique and modern so please do not post something that looks like a template from Cardwell!

Target Market(s)

Mainly to give to people aged 18-35. Most of my encounters will be casual so the card should have a "young" feeling to it. I rarely do anything in the corporate world so it doesn't have to be boring. It should give the impression that I'm the one they should go to if they need what I do (again it changes every weekend so I'll probably say the "what I do" part.

Industry/Entity Type

Wedding

Requirements
Must have
• Basically the contact information listed above
Nice to have
• I really like the colors Blue, Silver, and Purple. They don't have to necessarily all be there though. I do like the look of polished metal if that makes sense.
Should not have
• A template that resembles card-well. I'm in a point in my life where I'm working a lot of different markets/areas so the card does not need to have an address or address placeholder.

```html
<!DOCTYPE html>
<html lang="en">
<head>
<meta charset="utf-8">
<title>Gerald Minsky – Business Card</title>
<link rel="stylesheet" href="https://fonts.googleapis.com/css2?family=Montserrat:wght@700&family=Quicksand:wght@400;500&display=swap">
<style>
  :root {
    --backdrop: #b6bed0;
    --purple-deep: #7a1c8c;
    --purple-mid: #9a3aad;
    --purple-light: #b04fc0;
    --silver: #a9a8ad;
    --silver-light: #c4c3c8;
    --card-white: #e6e6e6;
    --ink-white: #ffffff;
    --ink-soft: #f1d9f5;
    --ink-grey: #6c6c6c;
  }
  * { margin: 0; padding: 0; box-sizing: border-box; }
  html, body {
    width: 1200px;
    height: 1003px;
    overflow: hidden;
    background: var(--backdrop);
  }
  .sheet {
    width: 1200px;
    height: 1003px;
    display: flex;
    flex-direction: column;
    align-items: center;
    justify-content: center;
    gap: 60px;
  }
  .card {
    position: relative;
    width: 700px;
    height: 400px;
    border-radius: 4px;
    overflow: hidden;
    box-shadow: 0 14px 30px rgba(60, 66, 90, 0.25);
  }

  /* Front: brushed purple fading into silver */
  .card-front {
    background:
      linear-gradient(200deg, var(--silver-light) 0%, var(--silver) 22%, rgba(169,168,173,0) 48%),
      linear-gradient(180deg, var(--purple-deep) 30%, var(--purple-light) 65%, var(--purple-mid) 85%, var(--purple-deep) 100%);
  }
  .card-front::after {
    content: "";
    position: absolute;
    inset: 0;
    background: repeating-linear-gradient(
      0deg,
      rgba(255,255,255,0.05) 0px,
      rgba(255,255,255,0.05) 1px,
      rgba(0,0,0,0.04) 2px,
      rgba(0,0,0,0) 3px
    );
    pointer-events: none;
  }
  .front-content {
    position: absolute;
    left: 190px;
    top: 118px;
    z-index: 1;
  }
  .holder-name {
    font-family: "Montserrat", sans-serif;
    font-weight: 700;
    font-size: 42px;
    letter-spacing: 1px;
    color: var(--ink-white);
    text-transform: uppercase;
    margin-left: 38px;
    text-shadow: 0 1px 2px rgba(0,0,0,0.2);
  }
  .contact-list {
    list-style: none;
    margin-top: 8px;
    font-family: "Quicksand", sans-serif;
    font-size: 17px;
    letter-spacing: 1.5px;
    color: var(--ink-soft);
  }
  .contact-list li { display: flex; line-height: 26px; }
  .contact-label { width: 78px; }

  /* Back: plain light card */
  .card-back {
    background: var(--card-white);
    display: flex;
    align-items: center;
    justify-content: center;
  }
  .greeting {
    font-family: "Quicksand", sans-serif;
    font-weight: 500;
    font-size: 19px;
    letter-spacing: 2px;
    color: var(--ink-grey);
  }
</style>
</head>
<body>
  <main class="sheet">
    <section class="card card-front" aria-label="Card front">
      <div class="front-content">
        <h1 class="holder-name">Gerald Minsky</h1>
        <ul class="contact-list">
          <li><span class="contact-label">e-mail</span><span>gerald@geraldminsky-demo.com</span></li>
          <li><span class="contact-label">tel</span><span>(555) 902-4416</span></li>
        </ul>
      </div>
    </section>
    <section class="card card-back" aria-label="Card back">
      <p class="greeting">Great meeting you!</p>
    </section>
  </main>
</body>
</html>
```